Online store website

Online store dealing on hoodies, joggers, trainers, baseball caps, trucker caps, winter hats, waist bands, jewelry sports and yoga suits , all women and men accessories.
All are my brand name Kel-vorwear.
I have a domain already

```html
<!DOCTYPE html>
<html lang="en">
<head>
<meta charset="UTF-8">
<title>Kel-vorwear — Online Store</title>
<link rel="stylesheet" href="https://fonts.googleapis.com/css2?family=Antonio:wght@400;500;600&family=Poppins:wght@400;500;600;700&display=swap">
<style>
  :root{
    --ink:#111111;
    --text:#2b2b2b;
    --muted:#444444;
    --accent:#fdb002;
    --white:#ffffff;
    --line:#222222;
    --about-bg:#e1dfdc;
    --footer-bg:#f6f6f6;
    --card-bg:#ececec;
    --display:"Antonio", sans-serif;
    --body:"Poppins", sans-serif;
  }
  *{margin:0;padding:0;box-sizing:border-box}
  html,body{width:1200px;height:4240px;overflow:hidden;background:var(--white)}
  body{position:relative;font-family:var(--body);color:var(--text)}
  .abs{position:absolute}
  .btn{position:absolute;display:flex;align-items:center;justify-content:center;background:var(--accent);color:var(--white);font-family:var(--body);font-weight:700;border-radius:40px;text-transform:uppercase;text-decoration:none}

  /* header */
  .site-header{position:absolute;left:0;top:0;width:1200px;height:89px;background:var(--white)}
  .brand{font-family:var(--display);font-weight:600;color:var(--ink);font-size:36px;line-height:1;letter-spacing:0.3px}
  .site-header .brand{position:absolute;left:127px;top:28px}
  .main-nav a{position:absolute;top:38px;font-family:var(--display);font-weight:500;font-size:17px;line-height:1;color:var(--ink);text-decoration:none}
  .header-icons svg{position:absolute;top:40px}
  .cart-count{position:absolute;left:1055px;top:34px;width:16px;height:16px;border-radius:50%;background:var(--accent);color:var(--ink);font-size:9px;font-weight:600;display:flex;align-items:center;justify-content:center}

  /* hero */
  .hero{position:absolute;left:0;top:89px;width:1200px;height:528px}
  .hero-photo{position:absolute;inset:0;background:linear-gradient(90deg,#1e2428 0%,#283034 48%,#4a4340 58%,#8c7064 68%,#7a645b 78%,#3a4044 88%,#55595b 100%)}
  .hero-kicker{position:absolute;left:129px;top:146px;font-family:var(--display);font-weight:500;color:var(--white);font-size:44px;line-height:1}
  .hero-title{position:absolute;left:127px;top:196px;font-family:var(--display);font-weight:600;color:var(--white);font-size:74px;line-height:1}
  .hero .btn{left:128px;top:293px;width:158px;height:53px;font-size:15px}

  .section-title{position:absolute;left:0;width:1200px;text-align:center;font-family:var(--display);font-weight:600;color:var(--ink);font-size:48px;line-height:1;text-transform:uppercase}

  /* collections */
  .collection{position:absolute;top:792px;width:278px;height:373px}
  .collection span{position:absolute;left:0;bottom:44px;width:100%;text-align:center;font-family:var(--display);font-weight:600;font-size:24px;line-height:1;color:var(--white)}
  .slider-rule{position:absolute;left:0;top:1246px;width:1200px;height:2px;background:var(--line)}
  .slider-arrow{position:absolute;top:1226px}

  /* products */
  .product{position:absolute;width:247px}
  .product-image{width:247px;height:256px}
  .product-name{margin-top:24px;font-size:19px;line-height:23px;color:var(--text);text-transform:uppercase;white-space:nowrap}
  .product-price{margin-top:14px;font-size:21px;font-weight:700;color:var(--ink)}
  .shop-btn{left:448px;width:304px;height:62px;font-size:19px}

  /* about */
  .about{position:absolute;left:0;top:2081px;width:1200px;height:516px;background:var(--about-bg)}
  .about-photo{position:absolute;left:592px;top:0;width:608px;height:516px;background:linear-gradient(135deg,#8d8a82 0%,#5c6a55 40%,#9b2a2a 70%,#b3a38e 100%)}
  .about h2{position:absolute;left:128px;top:134px;font-family:var(--display);font-weight:600;font-size:48px;line-height:1;color:var(--ink);text-transform:uppercase}
  .about p{position:absolute;left:127px;top:200px;width:380px;font-size:14.5px;line-height:20px;color:var(--text)}
  .about .btn{left:128px;top:334px;width:140px;height:46px;font-size:15px}

  /* accessory banners */
  .promo{position:absolute;top:3388px;height:368px}
  .promo h3{position:absolute;left:0;top:146px;width:100%;text-align:center;font-family:var(--display);font-weight:500;font-size:38px;line-height:1;color:var(--white);text-transform:uppercase}
  .promo .btn{top:205px;width:142px;height:40px;font-size:14px}

  /* footer */
  .site-footer{position:absolute;left:0;top:3819px;width:1200px;height:421px;background:var(--footer-bg)}
  .site-footer .brand{position:absolute;left:127px;top:80px;font-size:38px}
  .footer-about{position:absolute;left:127px;top:136px;width:245px;font-size:14px;line-height:24px;color:var(--text)}
  .footer-divider{position:absolute;top:74px;width:2px;height:247px;background:var(--line)}
  .footer-heading{position:absolute;top:82px;font-family:var(--display);font-weight:600;font-size:22px;line-height:1;color:var(--ink);text-transform:uppercase}
  .footer-links{position:absolute;top:128px;list-style:none;font-size:14px;line-height:30px;color:var(--text)}
  .newsletter-text{position:absolute;left:808px;top:130px;width:270px;font-size:14px;line-height:20px;color:var(--text)}
  .email-field{position:absolute;left:806px;top:178px;width:267px;height:53px;background:var(--white);border-radius:30px;font-size:13px;color:var(--muted);display:flex;align-items:center;padding-left:22px}
  .site-footer .subscribe{left:806px;top:242px;width:267px;height:54px;font-size:15px}
  .footer-rule{position:absolute;left:127px;top:342px;width:948px;height:1px;background:#bbbbbb}
  .copyright{position:absolute;right:125px;top:372px;font-size:15px;color:var(--text)}
</style>
</head>
<body>

<header class="site-header">
  <div class="brand">Kel-Vorwear</div>
  <nav class="main-nav">
    <a style="left:367px">Home</a>
    <a style="left:441px">Collections</a>
    <a style="left:548px">Men Accessories</a>
    <a style="left:691px">Women Accessories</a>
    <a style="left:853px">New</a>
  </nav>
  <div class="header-icons">
    <svg style="left:962px" width="18" height="18" viewBox="0 0 18 18" aria-label="Search"><circle cx="7.5" cy="7.5" r="5.5" fill="none" stroke="#111" stroke-width="2.5"/><line x1="11.5" y1="11.5" x2="16" y2="16" stroke="#111" stroke-width="2.5" stroke-linecap="round"/></svg>
    <svg style="left:1001px" width="17" height="18" viewBox="0 0 17 18" aria-label="Account"><circle cx="8.5" cy="5" r="4.5" fill="#111"/><path d="M0 18c0-5 3.8-8 8.5-8s8.5 3 8.5 8z" fill="#111"/></svg>
    <svg style="left:1039px" width="20" height="18" viewBox="0 0 20 18" aria-label="Cart"><path d="M0 1h3.5l3 10h10l2.5-7H5" fill="none" stroke="#111" stroke-width="2"/><path d="M5.5 4h13l-2.5 7h-10z" fill="#111"/><circle cx="8" cy="15.5" r="1.8" fill="#111"/><circle cx="15" cy="15.5" r="1.8" fill="#111"/></svg>
    <div class="cart-count">0</div>
  </div>
</header>

<section class="hero">
  <div class="hero-photo" role="img" aria-label="Model in a taupe hoodie and sunglasses against a dark slatted wall"></div>
  <div class="hero-kicker">WELCOME TO</div>
  <h1 class="hero-title">KEL-VORWEAR</h1>
  <a class="btn">Shop Now</a>
</section>

<h2 class="section-title" style="top:694px">Our Collections</h2>
<div class="collection" style="left:0;background:linear-gradient(160deg,#6b5a52,#2a2a2e 60%,#4a3e38)" role="img" aria-label="Model in a black hoodie"><span>Hoodies</span></div>
<div class="collection" style="left:308px;background:linear-gradient(160deg,#9cb46a,#6b6a4a 50%,#8d9aa3)" role="img" aria-label="Runner in olive joggers"><span>Joggers</span></div>
<div class="collection" style="left:614px;background:linear-gradient(160deg,#8a8f95,#6e3b33 45%,#3a3d42)" role="img" aria-label="Two athletes in training wear"><span>Trainers</span></div>
<div class="collection" style="left:922px;background:linear-gradient(160deg,#6f7a80,#c89a3a 50%,#d9c7a4)" role="img" aria-label="Model in a yellow knit winter hat"><span>Winter Hats</span></div>
<div class="slider-rule"></div>
<svg class="slider-arrow" style="left:549px" width="42" height="42" viewBox="0 0 42 42" aria-label="Previous"><circle cx="21" cy="21" r="19" fill="#fff" stroke="#111" stroke-width="2"/><path d="M29 21H13M19 15l-6 6 6 6" fill="none" stroke="#111" stroke-width="2"/></svg>
<svg class="slider-arrow" style="left:610px" width="42" height="42" viewBox="0 0 42 42" aria-label="Next"><circle cx="21" cy="21" r="19" fill="#fff" stroke="#111" stroke-width="2"/><path d="M13 21h16M23 15l6 6-6 6" fill="none" stroke="#111" stroke-width="2"/></svg>

<h2 class="section-title" style="top:1373px">All Products</h2>
<div class="product" style="left:127px;top:1476px"><div class="product-image" style="background:radial-gradient(ellipse 42% 46% at 50% 52%,#a9a9a9 0%,#bcbcbc 55%,var(--card-bg) 100%)" role="img" aria-label="Grey zip hoodie"></div><div class="product-name">Lorem ipsum dolor<br>sit ametadipisc</div><div class="product-price">$290.00</div></div>
<div class="product" style="left:415px;top:1476px"><div class="product-image" style="background:radial-gradient(ellipse 42% 46% at 50% 52%,#1e1e1e 0%,#3a3a3a 55%,var(--card-bg) 100%)" role="img" aria-label="Black joggers"></div><div class="product-name">Lorem ipsum dolor<br>sit ametadipisc</div><div class="product-price">$290.00</div></div>
<div class="product" style="left:703px;top:1476px"><div class="product-image" style="background:radial-gradient(ellipse 38% 34% at 50% 50%,#c66f0c 0%,#d9913a 55%,var(--card-bg) 100%)" role="img" aria-label="Orange beanie"></div><div class="product-name">Lorem ipsum dolor<br>sit ametadipisc</div><div class="product-price">$290.00</div></div>
<div class="product" style="left:991px;top:1476px"><div class="product-image" style="background:radial-gradient(ellipse 44% 28% at 55% 48%,#8e8c88 0%,#adaba7 55%,var(--card-bg) 100%)" role="img" aria-label="Grey baseball cap"></div><div class="product-name">Lorem ipsum dolor<br>sit ametadipisc</div><div class="product-price">$290.00</div></div>
<a class="btn shop-btn" style="top:1913px">Shop Our Products</a>

<section class="about">
  <h2>About Our Brand</h2>
  <p>Lorem ipsum dolor sit amet, consectetur adipi scing elit, sed do eiusmod tempor incididunt ut labore et dolore magna aliqua. Quis ipsum suspendisse ultrices gravida. Risus commodo viv erra maecenas accumsan lacus vel facilisis.</p>
  <a class="btn">Read More</a>
  <div class="about-photo" role="img" aria-label="Couple in green and red hoodies on a beach"></div>
</section>

<h2 class="section-title" style="top:2686px">Best Seller</h2>
<div class="product" style="left:127px;top:2788px"><div class="product-image" style="background:radial-gradient(ellipse 40% 46% at 50% 52%,#efb320 0%,#f0c454 55%,var(--card-bg) 100%)" role="img" aria-label="Yellow hoodie"></div><div class="product-name">Lorem ipsum dolor<br>sit ametadipisc</div><div class="product-price">$290.00</div></div>
<div class="product" style="left:415px;top:2788px"><div class="product-image" style="background:radial-gradient(ellipse 38% 46% at 50% 52%,#d2d2d2 0%,#dcdcdc 55%,var(--card-bg) 100%)" role="img" aria-label="Light grey joggers"></div><div class="product-name">Lorem ipsum dolor<br>sit ametadipisc</div><div class="product-price">$290.00</div></div>
<div class="product" style="left:703px;top:2788px"><div class="product-image" style="background:radial-gradient(ellipse 44% 44% at 50% 52%,#c4161c 0%,#d24a4d 55%,var(--card-bg) 100%)" role="img" aria-label="Red zip hoodie"></div><div class="product-name">Lorem ipsum dolor<br>sit ametadipisc</div><div class="product-price">$290.00</div></div>
<div class="product" style="left:991px;top:2788px"><div class="product-image" style="background:radial-gradient(ellipse 44% 28% at 55% 48%,#8e8c88 0%,#adaba7 55%,var(--card-bg) 100%)" role="img" aria-label="Grey baseball cap"></div><div class="product-name">Lorem ipsum dolor<br>sit ametadipisc</div><div class="product-price">$290.00</div></div>
<a class="btn shop-btn" style="top:3225px">Shop Our Products</a>

<div class="promo" style="left:0;width:584px;background:linear-gradient(135deg,#7c6a55,#3d3a34 50%,#8a6e52)" role="img" aria-label="Leather handbags on display">
  <h3>Women Accessories</h3><a class="btn" style="left:201px">Shop Now</a>
</div>
<div class="promo" style="left:616px;width:584px;background:linear-gradient(135deg,#6f4e3a,#a39380 50%,#8b7a68)" role="img" aria-label="Wristwatch with a brown leather strap">
  <h3>Men Accessories</h3><a class="btn" style="left:241px">Shop Now</a>
</div>

<footer class="site-footer">
  <div class="brand">Kel-Vorwear</div>
  <p class="footer-about">Lorem ipsum dolor sit amet, consectetur adipiscing elit, sed do eiusmod tempor incididunt ut labore et dolore magna aliqua. Quis ipsum suspendisse.</p>
  <div class="footer-divider" style="left:395px"></div>
  <div class="footer-heading" style="left:448px">Products</div>
  <ul class="footer-links" style="left:448px"><li>hoodies</li><li>joggers</li><li>trainers</li><li>baseball caps</li><li>trucker caps</li><li>winter hats</li></ul>
  <ul class="footer-links" style="left:584px"><li>waist bands</li><li>jewelry sports</li><li>yoga suits</li><li>women accessories</li><li>men accessories</li></ul>
  <div class="footer-divider" style="left:755px"></div>
  <div class="footer-heading" style="left:808px">Newsletter</div>
  <p class="newsletter-text">Receive access to VIP discounts, new product launches and more.</p>
  <div class="email-field">Email:</div>
  <a class="btn subscribe">Subscribe</a>
  <div class="footer-rule"></div>
  <svg class="abs" style="left:127px;top:362px" width="42" height="42" viewBox="0 0 42 42" aria-label="Social link"><circle cx="21" cy="21" r="19" fill="none" stroke="#111" stroke-width="2"/></svg>
  <div class="copyright">Copyright © 2025 All rights reserved - Kel-vorwear</div>
</footer>

</body>
</html>
```